Modern website for custom software development company
Tessaro
Creative Brief
Software
http://tessaro.example
Custom Software Development company Tessaro Software Solutions based in the Vancouver, BC, Canada area.
http://quorvane.example/
http://madebyheron.example/
http://lumenstudio.example/
Logo is https://files.example/s/k2p9wq71zx4rmtn/logo.jpg
Hi PH,
Please check private message.
Thanks
Pelvostudio
The navigation items will be Home, Portfolio, About, and Contact.
I would also like to have a project planner such as this http://madebyheron.example/planner
Adding some more notes:
I'd prefer the page elements to be allowed to breathe. Take a look at https://www.vexaro.example/partners/ and the rest of the websites in the brief.
I am starting up in the business, I don't want to fake out being bigger than I actually am, so please avoid a corporate look.
I'm also looking for a touch of originality.
Thanks,
Dale

```html
<!DOCTYPE html>
<html lang="en">
<head>
<meta charset="utf-8">
<title>Tessaro — Custom Software Development</title>
<link rel="stylesheet" href="https://fonts.googleapis.com/css2?family=Open+Sans:wght@300;400;600;700&family=Titillium+Web:wght@300;400;600&family=Exo+2:wght@400;500&display=swap">
<style>
:root{
  --ink:#2d323b;
  --ink-soft:#3a3f48;
  --orange:#e8501e;
  --planner:#d9500f;
  --sun:#ffb21c;
  --olive:#a0a087;
  --mist:#efefef;
  --card:#8d919c;
  --disc:#8a8e98;
  --muted:#6c7078;
  --white:#ffffff;
  --foot:#e3e3e3;
}
*{margin:0;padding:0;box-sizing:border-box}
html,body{width:1200px;height:2769px;overflow:hidden}
body{font-family:"Open Sans",Arial,sans-serif;background:var(--white);color:var(--ink);position:relative}
h1,h2,h3{font-weight:400}
section,header,footer{position:absolute;left:0;width:1200px;overflow:hidden}
.abs{position:absolute}
.center{left:0;width:1200px;text-align:center}

/* header */
.site-header{top:0;height:83px;background:var(--ink)}
.brand{left:150px;top:28px;display:flex;align-items:center;gap:8px}
.brand-mark{width:20px;height:20px;background:var(--orange)}
.brand-name{font-family:"Open Sans",sans-serif;font-weight:600;font-size:17px;color:var(--white);letter-spacing:1px}
.nav{right:0;top:0;height:83px}
.nav a{position:absolute;top:52px;font-family:"Exo 2",sans-serif;font-size:13px;letter-spacing:1.2px;color:var(--white);text-decoration:none}
.nav .active-tab{position:absolute;left:683px;top:0;width:72px;height:83px;background:var(--orange)}
.nav .active-line{position:absolute;left:695px;top:71px;width:48px;height:2px;background:var(--white)}

/* hero */
.hero{top:83px;height:479px;background:linear-gradient(180deg,#5f6f86 0%,#8a7f86 30%,#a47f6c 52%,#5a3a2c 72%,#2a1c18 100%)}
.hero-title{left:159px;top:271px;width:876px;height:55px;background:rgba(232,80,30,.82);color:var(--white);font-family:"Titillium Web",sans-serif;font-weight:400;font-size:50px;line-height:55px;text-align:center;white-space:nowrap;overflow:hidden}
.hero-sub{top:348px;color:var(--white);font-size:28px;line-height:41px;font-weight:400}

/* different */
.different{top:562px;height:296px;background:var(--white)}
.different h2{top:30px;font-weight:300;font-size:44px;color:var(--orange)}
.different .lead{top:90px;font-size:14.5px;color:var(--ink)}
.different .body{left:150px;width:900px;top:132px;text-align:center;font-size:13px;line-height:23.5px;color:var(--muted);letter-spacing:.3px}

/* services */
.services{top:858px;height:489px;background:var(--ink)}
.services h2{top:20px;font-weight:300;font-size:44px;color:var(--white)}
.services .sub{top:90px;font-weight:300;font-size:29px;color:#a6aab2}
.svc{position:absolute;top:163px;width:226px;height:271px;text-align:center}
.svc.is-active{background:var(--card)}
.svc .disc{position:absolute;left:67px;top:20px;width:92px;height:92px;border-radius:50%;background:var(--disc);display:flex;align-items:center;justify-content:center}
.svc.is-active .disc{background:#3c414a}
.svc h3{position:absolute;top:122px;left:0;width:226px;font-weight:400;font-size:15px;line-height:17px;color:var(--white)}
.svc p{position:absolute;top:171px;left:10px;width:206px;font-size:12.5px;line-height:17px;color:#8a8e97}
.svc.is-active p{color:var(--white)}
.svc .more{position:absolute;top:229px;left:0;width:226px;font-size:12px;font-weight:700;color:#c9ccd1}
.svc.is-active .more{color:#b5b8bf}
.binary{font-family:"Open Sans",sans-serif;font-size:17px;line-height:21px;letter-spacing:5px;color:var(--white);text-align:center;padding-left:4px}

/* process */
.process{top:1347px;height:438px;background:var(--olive)}
.process h2{top:27px;font-weight:300;font-size:43px;color:var(--white)}
.process .sub{top:100px;font-weight:300;font-size:18px;color:#eeeee4}
.step{position:absolute;width:240px}
.step .ico{position:absolute;left:0;top:4px}
.step h3{position:absolute;left:38px;top:0;font-weight:400;font-size:29px;line-height:36px;color:var(--white);white-space:nowrap}
.step h3 span{color:#e2e2d2;font-weight:300}
.step p{position:absolute;left:38px;top:40px;width:175px;font-size:11px;line-height:15.5px;color:var(--white)}
.flow{position:absolute}

/* portfolio */
.portfolio{top:1785px;height:397px;background:var(--mist)}
.portfolio h2{top:20px;font-weight:300;font-size:43px;color:var(--ink)}
.portfolio .sub{top:77px;font-weight:300;font-size:26px;color:var(--ink-soft)}
.shot-frame{left:213px;top:150px;width:312px;height:191px;background:var(--white);border:1px solid #d0d0d0;padding:5px}
.shot{width:100%;height:100%;background:linear-gradient(120deg,#3e5d86 0%,#7a98b9 50%,#c9d4de 100%)}
.project-name{left:637px;top:146px;font-size:29px;font-weight:400;color:var(--orange)}
.project-ico{left:575px;top:148px}
.project-text{left:570px;top:196px;width:440px;font-size:12.5px;line-height:21.5px;color:var(--muted)}
.view-btn{left:568px;top:292px;width:134px;height:32px;background:var(--white);border-bottom:2px solid #cfcfcf;font-size:16px;font-weight:600;color:var(--ink);line-height:31px;text-align:center}
.pager{top:200px}

/* planner */
.planner{top:2182px;height:277px;background:var(--planner)}
.planner .ring{left:160px;top:64px}
.planner h2{left:350px;top:48px;font-weight:300;font-size:44px;color:var(--white)}
.planner .pitch{left:350px;top:113px;font-weight:300;font-size:28px;line-height:29px;color:var(--sun)}
.launch-btn{left:352px;top:197px;width:116px;height:32px;background:#c9c6c3;color:var(--orange);font-size:16px;font-weight:600;text-align:center;line-height:32px}

/* contact */
.contact{top:2459px;height:264px;background:var(--ink)}
.contact h2{top:40px;font-weight:300;font-size:26px;color:var(--white)}
.contact .mark{left:156px;top:123px;width:54px;height:54px;background:var(--orange)}
.contact .email{left:230px;top:100px;font-size:30px;font-weight:300;color:var(--orange)}
.contact .addr{left:231px;top:138px;font-size:15px;line-height:18px;color:var(--white)}
.contact .call{left:233px;top:206px;font-size:15px;color:var(--white);display:flex;align-items:center;gap:6px}
.contact .call b{font-weight:400;color:var(--orange)}
.map{left:637px;top:99px;width:398px;height:111px;background:linear-gradient(135deg,#e6e3db,#d9d6cc)}
.map-link{left:638px;top:217px;font-size:11px;font-weight:700;color:#cfd2d8}

/* footer */
.site-footer{top:2723px;height:46px;background:var(--foot)}
.social{position:absolute;top:9px;width:28px;height:28px;border-radius:50%;background:#cfcfcf}
.legal{left:339px;top:16px;font-size:11px;color:var(--ink-soft)}
.copy{left:878px;top:15px;font-size:11px;color:#8c8c8c}
.foot-brand{left:974px;top:12px;font-size:15px;font-weight:600;letter-spacing:1px;color:var(--ink-soft)}
</style>
</head>
<body>

<header class="site-header">
  <div class="abs brand"><span class="brand-mark"></span><span class="brand-name">TESSARO</span></div>
  <nav class="abs nav" style="left:0;width:1200px">
    <span class="active-tab"></span>
    <a href="#" style="left:698px">HOME</a>
    <span class="active-line"></span>
    <a href="#" style="left:773px">ABOUT</a>
    <a href="#" style="left:853px">PORTFOLIO</a>
    <a href="#" style="left:965px">CONTACT</a>
  </nav>
</header>

<section class="hero" role="img" aria-label="Photograph of snow-capped mountains at sunset">
  <h1 class="abs hero-title">Custom Software Development Company</h1>
  <p class="abs center hero-sub">We pride ourselves in being very responsive in customer service,<br>strong on quality and effective at getting the job done.</p>
</section>

<section class="different">
  <h2 class="abs center">How we are different</h2>
  <p class="abs center lead">Tessaro Software Solutions based in the Vancouver, BC, Canada</p>
  <p class="abs body">Lorem ipsum dolor sit amet, consectetuer adipiscing elit, sed diam nonummy nibh euismod tincidunt ut laoreet dolore magna aliquam erat volutpat. Ut wisi enim ad minim veniam, quis nostrud exerci tation ullamcorper suscipit lobortis nisl &nbsp;aliquip ex ea commodo consequat. Duis autem vel eum iriure dolor in hendrerit vulputate velit esse molestie consequat, vel illum dolore eu feugiat nulla facilisis at vero eros et accumsan et iusto odio dignissim qui blandit praesent luptatu<br>zzril delenit augue duis dolore te feugait nulla facilisi.</p>
</section>

<section class="services">
  <h2 class="abs center">Development Services</h2>
  <p class="abs center sub">Providing the best software so you can concentrate on your thing</p>

  <article class="svc" style="left:148px">
    <div class="disc"><div class="binary">0101<br>1011<br>0110</div></div>
    <h3>Custom Software<br>Development</h3>
    <p>Lorem ipsum dolo consectetuer adipiscing elit,Lorem ipsum uismod tincidunt ut</p>
    <div class="more">More</div>
  </article>

  <article class="svc is-active" style="left:374px">
    <div class="disc">
      <svg width="54" height="54" viewBox="0 0 54 54"><g fill="#fff" transform="translate(27 27)">
        <circle r="17"/>
        <rect x="-5" y="-26" width="10" height="12"/><rect x="-5" y="14" width="10" height="12"/>
        <rect x="-26" y="-5" width="12" height="10"/><rect x="14" y="-5" width="12" height="10"/>
        <rect x="-5" y="-26" width="10" height="12" transform="rotate(45)"/><rect x="-5" y="14" width="10" height="12" transform="rotate(45)"/>
        <rect x="-26" y="-5" width="12" height="10" transform="rotate(45)"/><rect x="14" y="-5" width="12" height="10" transform="rotate(45)"/>
      </g><circle cx="27" cy="27" r="7" fill="#3c414a"/></svg>
    </div>
    <h3>Open Source<br>Solution</h3>
    <p>Lorem ipsum dolo consectetuer adipiscing elit,Lorem ipsum uismod tincidunt ut</p>
    <div class="more">More</div>
  </article>

  <article class="svc" style="left:600px">
    <div class="disc">
      <svg width="50" height="44" viewBox="0 0 50 44"><rect x="2" y="2" width="46" height="30" rx="2" fill="none" stroke="#fff" stroke-width="4"/><g fill="#fff"><rect x="9" y="9" width="6" height="5"/><rect x="17" y="9" width="6" height="5"/><rect x="25" y="9" width="6" height="5"/><rect x="33" y="9" width="6" height="5"/><rect x="9" y="17" width="6" height="5"/><rect x="17" y="17" width="6" height="5"/><rect x="25" y="17" width="6" height="5"/><rect x="33" y="17" width="6" height="5"/><rect x="21" y="32" width="8" height="6"/><rect x="14" y="38" width="22" height="4"/></g></svg>
    </div>
    <h3>Web<br>Development</h3>
    <p>Lorem ipsum dolo consectetuer adipiscing elit,Lorem ipsum uismod tincidunt ut</p>
    <div class="more">More</div>
  </article>

  <article class="svc" style="left:826px">
    <div class="disc">
      <svg width="30" height="50" viewBox="0 0 30 50"><rect x="2" y="2" width="26" height="46" rx="4" fill="none" stroke="#fff" stroke-width="4"/><rect x="7" y="9" width="16" height="28" fill="#fff"/><circle cx="15" cy="42" r="2.5" fill="#fff"/></svg>
    </div>
    <h3>Mobile App<br>Development</h3>
    <p>Lorem ipsum dolo consectetuer adipiscing elit,Lorem ipsum uismod tincidunt ut</p>
    <div class="more">More</div>
  </article>
</section>

<section class="process">
  <h2 class="abs center">Our Work Process</h2>
  <p class="abs center sub">Providing the best software so you can concentrate on your thing</p>

  <div class="step" style="left:194px;top:158px">
    <svg class="ico" width="28" height="34" viewBox="0 0 28 34"><path d="M2 2h16l8 8v22H2z" fill="none" stroke="#8b8b74" stroke-width="3"/><g stroke="#8b8b74" stroke-width="2"><path d="M7 14h14M7 19h14M7 24h14"/></g></svg>
    <h3><span>1</span> Brif</h3>
    <p>Lorem ipsum dolor sit,Facilisis at vero eros et accumsan et iusto odio dignissim qui</p>
  </div>
  <div class="step" style="left:460px;top:158px">
    <svg class="ico" width="34" height="34" viewBox="0 0 34 34"><g fill="#8b8b74"><circle cx="17" cy="6" r="5"/><circle cx="6" cy="17" r="5"/><circle cx="28" cy="17" r="5"/><circle cx="17" cy="28" r="5"/></g></svg>
    <h3><span>2</span> Planning</h3>
    <p>Lorem ipsum dolor sit,Facilisis at vero eros et accumsan et iusto odio dignissim qui</p>
  </div>
  <div class="step" style="left:763px;top:158px">
    <svg class="ico" width="34" height="34" viewBox="0 0 34 34"><g fill="none" stroke="#8b8b74" stroke-width="5" stroke-dasharray="4 3"><circle cx="12" cy="22" r="8"/><circle cx="26" cy="8" r="5"/></g></svg>
    <h3><span>3</span> Development</h3>
    <p>Lorem ipsum dolor sit,Facilisis at vero eros et accumsan et iusto odio dignissim qui</p>
  </div>
  <div class="step" style="left:326px;top:292px">
    <svg class="ico" width="34" height="34" viewBox="0 0 34 34"><circle cx="13" cy="13" r="10" fill="none" stroke="#8b8b74" stroke-width="3"/><path d="M20 20l11 11" stroke="#8b8b74" stroke-width="5" stroke-linecap="round"/></svg>
    <h3><span>4</span> Testing</h3>
    <p>Lorem ipsum dolor sit,Facilisis at vero eros et accumsan et iusto odio dignissim qui</p>
  </div>
  <div class="step" style="left:591px;top:292px">
    <svg class="ico" width="36" height="32" viewBox="0 0 36 32"><g fill="#8b8b74"><rect x="2" y="6" width="20" height="16"/><path d="M22 11h7l5 6v5H22z"/><circle cx="9" cy="25" r="4"/><circle cx="28" cy="25" r="4"/></g></svg>
    <h3><span>5</span> Deliver</h3>
    <p>Lorem ipsum dolor sit,Facilisis at vero eros et accumsan et iusto odio dignissim qui</p>
  </div>

  <svg class="flow" style="left:410px;top:222px" width="60" height="22" viewBox="0 0 60 22"><path d="M2 6q25 16 52 4" fill="none" stroke="#fff" stroke-width="1.5"/><path d="M46 5l9 5-8 6" fill="none" stroke="#fff" stroke-width="1.5"/></svg>
  <svg class="flow" style="left:716px;top:222px" width="60" height="22" viewBox="0 0 60 22"><path d="M2 6q25 16 52 4" fill="none" stroke="#fff" stroke-width="1.5"/><path d="M46 5l9 5-8 6" fill="none" stroke="#fff" stroke-width="1.5"/></svg>
  <svg class="flow" style="left:550px;top:356px" width="60" height="22" viewBox="0 0 60 22"><path d="M2 6q25 16 52 4" fill="none" stroke="#fff" stroke-width="1.5"/><path d="M46 5l9 5-8 6" fill="none" stroke="#fff" stroke-width="1.5"/></svg>
</section>

<section class="portfolio">
  <h2 class="abs center">Our Work Portfolio</h2>
  <p class="abs center sub">We deliver top quality products and services</p>

  <svg class="abs pager" style="left:140px" width="22" height="46" viewBox="0 0 22 46"><path d="M19 2L4 23l15 21" fill="none" stroke="#c8c8c8" stroke-width="2"/></svg>
  <svg class="abs pager" style="left:1040px" width="22" height="46" viewBox="0 0 22 46"><path d="M3 2l15 21L3 44" fill="none" stroke="#c8c8c8" stroke-width="2"/></svg>

  <div class="abs shot-frame"><div class="shot" role="img" aria-label="Photograph of a hand touching app icons on a glass screen"></div></div>

  <svg class="abs project-ico" width="50" height="36" viewBox="0 0 50 36"><path d="M12 32a10 10 0 0 1 0-20 14 14 0 0 1 27 2 9 9 0 0 1 0 18z" fill="#9a9a9a"/><path d="M25 14v14M19 22l6 6 6-6" fill="none" stroke="#efefef" stroke-width="3"/></svg>
  <h3 class="abs project-name">Project Name</h3>
  <p class="abs project-text">Lorem ipsum dolor sit amet, consectetuer adipiscing elit, sed diam nonummy nibh euismod tincidunt ut laoreet dolore magna aliquam erat volutpat. Ut wisi enim ad minim veniam, quis nostrud exerci tation ullamcorper suscipit lobortis nisl &nbsp;aliquip ex ea commodo consequat.</p>
  <div class="abs view-btn">View project</div>
</section>

<section class="planner">
  <svg class="abs ring" width="160" height="160" viewBox="0 0 160 160">
    <circle cx="80" cy="80" r="77" fill="none" stroke="#8a2a06" stroke-width="1.5" stroke-dasharray="3 3"/>
    <circle cx="80" cy="80" r="70" fill="#fff"/>
    <g transform="translate(80 80) rotate(45)" fill="#2d323b">
      <path d="M0-30c9 8 11 22 8 36H-8c-3-14-1-28 8-36z"/>
      <path d="M-8 0l-9 12 9-2zM8 0l9 12-9-2z"/>
      <path d="M-5 10h10l-5 14z"/>
    </g>
    <circle cx="80" cy="80" r="4" fill="#fff" transform="translate(-4 -4)"/>
  </svg>
  <h2 class="abs">Project Planner</h2>
  <p class="abs pitch">Interested in working with us?<br>Launch our proposal planner to get started.</p>
  <div class="abs launch-btn">Launch it</div>
</section>

<section class="contact">
  <h2 class="abs center">Do not hesitate to contact us and we will let you know more.</h2>
  <div class="abs mark"></div>
  <p class="abs email">info@tessaro.example</p>
  <p class="abs addr">Dale Morrow Consulting Inc<br>4410 Cedar Row, Suite 12<br>Brookvale, BC, CA</p>
  <p class="abs call"><svg width="14" height="14" viewBox="0 0 14 14"><path d="M3 1l3 3-2 2c1 2 2 3 4 4l2-2 3 3-2 2C6 13 1 8 1 3z" fill="#c9ccd1"/></svg><b>Call:</b> 555-0142-3390</p>
  <div class="abs map" role="img" aria-label="Street map showing the office location"></div>
  <p class="abs map-link">See directions on Mapvia</p>
</section>

<footer class="site-footer">
  <span class="social" style="left:157px"></span>
  <span class="social" style="left:190px"></span>
  <span class="social" style="left:223px"></span>
  <span class="social" style="left:257px"></span>
  <span class="social" style="left:290px"></span>
  <p class="abs legal">Privacy &amp; Terms</p>
  <p class="abs copy">Copyright ©2013</p>
  <p class="abs foot-brand">TESSARO</p>
</footer>

</body>
</html>
```